Mobile Repair Service on location needs a Web Design

We are starting a new mobile device repair service called Gadget Haven and our website needs a design!

Hello Designers!
First, we'd like to make clear this is more than a simple web design contest, we want the designers to create an idea. We want someone who can create the whole theme of the service's we provide. We want someone that can help design our visual branding, help us communicate a sentiment. And we are willing to pay for that.

Who are we?
Our company is based in Rotterdam, the Netherlands. We provide different services for all kinds of electronic devices. The kind of services we provide are, among other things, installations of hardware and software and the repair of broken or malfunctioning devices.
We are starting a new service that offers mobile device repairs on location, be it at the home of our customers, their office, or any other place. Just give us the address and we will come to you for the repair job. This is also our main USP. We have multiple skilled engineers who drive trough the country on a daily basis and can be on location within a working day. Repair is done immediately onsite while the customer waits. At this stage we will start with the smartphone product-group within the mobile devices. In a second phase we might also add tablets.
People don't want to be without their phone for weeks because of some parts that needed to be ordered by a repair center they had to sent their phone to. We offer a fully functional mobile repair center in the form of specially customized vans. These vans have all the tools and utilities needed by our engineers to safely repair your mobile device. Your phone is being repaired directly in front of you, the next business-day, on a location you desire.

For this new service we are creating a website called Gadget Haven. The website needs a story and matching design and this is where you come in. We are not looking for a simple template design we can get from any place. We need a story. We want you to create an idea, build a unique theme or vision that helps sell the product/service. This goes beyond the design of the website. We need the whole package, the design you are creating needs to have returning elements like icons, color use, images, maybe even characters etc. You name it! There needs to be a common thread in the design so we can reuse elements in, for example, the email templates, the work order or receipt we give to our customers (we may contact the winner of the contest to design these for us as well!).

The name 'Gadget Haven' is chosen. Haven (short for rehabilitate) has a bold and playful tone to it and the design needs to reflect the name. So we're looking for a somewhat playful and cheeky design. Definitely not too serious and definitely modern. We already got a logo that we love and that fit's this description (see attached design documents for the logo). It's bold, powerful and fun. Our web design needs to reflect this as well and has to fit in with our logo.
We would really like it if the design somehow incorporates elements that highlight our unique selling points (repairs on location, we come to you etc.). We would really like some form of story telling in the design. Think clumsy people breaking their phones. Teenagers in tears because they have no access to their friends. People nowadays have the need to always be 'connected'. What happens when your phone is broken or malfunctioning? We're handling tech, we are nerds and a little bit weird, but we're professionals and here to help you with your problem. The sentiment Wire Troop tries to communicate is something we really like. We're looking for fresh idea's, anything goes!

In an overview all Unique Selling Points of the Gadget haven service:
- Professional service on location. Don’t ship to us we will come to you!
- Clear pricing upfront. No hidden cost.
- Next business-day repair.
- Backed by a professional call center open 12 hours a day and open on a Saturday as well
- Backed by a professional repair center with more then 12 years of experience
- Repair is done by certified engineers
- 1 year warranty on the repair

The process:
The main function of our website will be for customers to make a repair request. A customer will visit our website and can make a repair request immediately by going through a 'request-order-flow'. In this flow he or she will need to fill in some forms and can select wich type/model/brand of mobile device he or she has and what parts need to be repaired. After a request is placed we will call the customer back (within an hour) for a short intake and to set a date/time and location. Our engineer will meet the customer at the specified location and will repair the device onsite in one of our mobile repair centers, which is a specialized van equipped with all the tools needed for device restorations.
So in short the steps are:
- Choose your device and repair job
- Place the order
- Get a callback within the hour
- Set date and location
- We will come to you.

Website functionality:
Our website is our main form of communication. So the sentiment we want to communicate needs be reflected in the design. We need a main/front page designed (preferably a long scrolling page design) containing:
1. Customers will be able to request a repair job directly on our website. So there will need to be a prominent button/link at the top of our main page that will bring the customer to this 'request-order-flow'. This is the main flow which needs to be full focus on the front page. All other items are secondary.
2. The general information of who we are and what we do, and why the customer should choose us. Preferably in short bullet-point type keywords/sentences with icons or other visual cues. See our unique selling points to get an idea of the information that will be displayed here.
3. There needs to be a section that will explain the process (see above) of a repair request step-by- step, again in brief short key sentences and with (custom) icons.
4. There needs to be a section that explains to the customer he/she can always contact us if they are not sure what the problem is with their device, and for this reason are not sure what repair request they should order.
5. We want to implement some functionality that display customer ratings or customer reviews. So there needs to be room for some kind of widget of plugin we're going to implement which shows these reviews.
6. A 'For business section' where we will explain all the options we provide for corporate clients.
7. Social media links.
8. There needs to be a menu with buttons that leads to the all sections described in the previous points.

For now, we need a design for our front page. In the second phase, when we have picked our winner, we may ask the winner to design the page(s) for our request workflow as well.

EDIT:
Finally, we have a very specific order in mind for the different segments of our website. We would like you to add some more segments that were not in our original brief as well:

1. Top header with order/request button. (should instantly make clear our main USP, we do repairs on location)
2. Our process
3. Our unique selling points / why choose us
4. The kind of repairs we do (broken screens, broken batteries, water damage, broken camera's, no sound etc.)
5. A 'meet our team' section, where we introduce some of our engineers
6. A 'contact us for any questions' section/
7. Testimonials/user reviews
8. A section where we show key performance indicators
9. 'For businesses' sections
10.'Subscribe for newsletter' field
11. Social media buttons

Industry/Entity Type

It Service

Number of Pages Required

1 page

Font styles to use
Sans Serif

Requirements
Must have
• a main/front page, design only
• custom icons/images for banners, adverts online and in print (high res)
Nice to have
• Storytelling in our design.
• Design that fits with our brand new logo.
• Elements like icons to have a flat design.
• Keep in mind that the website will need to be responsive when designing! (Ideally provide an example of the mobile design as well)
• Create a fun and trustworthy feeling.

```html
<!DOCTYPE html>
<html lang="en">
<head>
<meta charset="utf-8">
<title>Gadget Haven — Mobile Repair On Location</title>
<link href="https://fonts.googleapis.com/css2?family=Roboto:wght@300;400;500;700;900&display=swap" rel="stylesheet">
<style>
:root{
  --orange:#ff5e22;
  --orange-soft:#ff7a45;
  --charcoal:#3a3d3f;
  --ink:#2f3234;
  --body:#5a5d60;
  --line:#cfd2d4;
  --muted:#a3a6a9;
  --white:#ffffff;
}
*{box-sizing:border-box;margin:0;padding:0}
html,body{width:1119px;height:1200px;overflow:hidden;background:var(--white);font-family:"Roboto",Arial,sans-serif}
.page{position:relative;width:1119px;height:1200px}

.topbar{position:absolute;left:0;top:0;width:1119px;height:84px;background:var(--charcoal);border-bottom:2px solid var(--orange)}
.brand{position:absolute;left:80px;top:0;width:203px;height:116px;background:var(--white);box-shadow:0 3px 8px rgba(0,0,0,.15);display:flex;align-items:center;justify-content:center;gap:10px;z-index:3}
.brand-dot{width:26px;height:26px;border-radius:50%;background:var(--orange)}
.brand-name{font-weight:900;font-size:22px;line-height:1;color:var(--charcoal);letter-spacing:.5px}
.nav{position:absolute;top:0;left:460px;display:flex;height:84px;list-style:none}
.nav li{height:84px;display:flex;align-items:center;padding-top:4px;font-size:15px;color:var(--white);text-transform:uppercase}
.nav .active{background:var(--white);color:var(--orange);width:74px;justify-content:center}
.nav .about{margin-left:35px}
.nav .services{margin-left:51px}
.nav .testimonial{margin-left:51px}
.nav .contact{margin-left:51px}

.hero{position:absolute;left:0;top:84px;width:1119px;height:464px;background:var(--orange)}
.hero-devices{position:absolute;left:74px;top:110px;width:600px;height:324px;border-radius:18px;background:linear-gradient(160deg,#f4f4f6 0%,#d9dbe0 55%,#ff8a5a 100%);opacity:.9}
.hero-title{position:absolute;left:264px;top:135px;font-size:66px;font-weight:900;color:var(--white);letter-spacing:-1px;text-shadow:0 2px 6px rgba(0,0,0,.15)}

.order{position:absolute;left:738px;top:117px;width:304px;height:633px;background:var(--white);box-shadow:0 2px 5px rgba(0,0,0,.22);z-index:2}
.order-head{height:66px;background:var(--charcoal);color:var(--white);font-weight:300;font-size:24px;display:flex;align-items:center;justify-content:center}
.field-label{position:absolute;left:22px;font-size:13.5px;font-weight:500;color:var(--ink)}
.select{position:absolute;display:flex;align-items:center;border:1px solid var(--line);color:var(--muted);font-size:13px;background:var(--white)}
.select span{flex:1;padding-left:14px;white-space:nowrap;overflow:hidden}
.select .chev{height:100%;border-left:1px solid var(--line);display:flex;align-items:center;justify-content:center}
.select.tiny{font-size:8.5px}
.select.tiny span{padding-left:7px}
.note{position:absolute;left:21px;top:480px;width:264px;height:68px;border:1px solid var(--line)}
.submit{position:absolute;left:80px;top:567px;width:143px;height:43px;background:var(--charcoal);color:var(--white);font-weight:700;font-size:15px;display:flex;align-items:center;justify-content:center;letter-spacing:.3px}

.about-kicker{position:absolute;left:82px;top:636px;font-size:50px;font-weight:400;color:var(--ink);letter-spacing:26px}
.about-title{position:absolute;left:80px;top:688px;font-size:70px;line-height:1;color:var(--ink);letter-spacing:-1px}
.about-title b{font-weight:900}
.about-title em{font-style:normal;font-weight:400;color:var(--orange)}
.about-device{position:absolute;left:94px;top:794px;width:280px;height:381px;border-radius:24px;background:linear-gradient(170deg,#c9cbcf 0%,#1aa3d6 30%,#0c6fa8 75%,#9a9da2 100%)}
.about-copy{position:absolute;left:409px;top:804px;width:632px;font-size:13px;line-height:21.3px;color:var(--body)}
.about-copy p{margin-bottom:11px}
.about-copy strong{color:#45484b;font-weight:500}
.read-more{position:absolute;left:408px;top:1117px;width:92px;height:34px;background:var(--orange);color:var(--white);font-size:11.5px;font-weight:500;display:flex;align-items:center;justify-content:center}
</style>
</head>
<body>
<div class="page">

  <header class="topbar">
    <ul class="nav">
      <li class="active">Home</li>
      <li class="about">About us</li>
      <li class="services">Services</li>
      <li class="testimonial">Testimonial</li>
      <li class="contact">Contact us</li>
    </ul>
  </header>
  <div class="brand"><div class="brand-dot"></div><div class="brand-name">GADGET<br>HAVEN</div></div>

  <section class="hero">
    <div class="hero-devices" role="img" aria-label="White smartphone and tablet lying on the orange background"></div>
    <h1 class="hero-title">WELCOME TO!</h1>
  </section>

  <form class="order">
    <div class="order-head">Request Order-Flow</div>

    <div class="field-label" style="top:92px">Choose your device and repair job :</div>
    <div class="select" style="left:21px;top:127px;width:264px;height:47px"><span>Select repair job</span>
      <div class="chev" style="width:34px"><svg width="12" height="8" viewBox="0 0 12 8"><path d="M1.5 1.5 6 6l4.5-4.5" fill="none" stroke="#2f3234" stroke-width="2"/></svg></div></div>

    <div class="field-label" style="top:186px">Place the order :</div>
    <div class="select" style="left:21px;top:221px;width:264px;height:47px"><span>Select order</span>
      <div class="chev" style="width:34px"><svg width="12" height="8" viewBox="0 0 12 8"><path d="M1.5 1.5 6 6l4.5-4.5" fill="none" stroke="#2f3234" stroke-width="2"/></svg></div></div>

    <div class="field-label" style="top:282px;left:21px">Get a callback with the hour :</div>
    <div class="select" style="left:21px;top:316px;width:85px;height:35px"><span>Hour</span>
      <div class="chev" style="width:30px"><svg width="11" height="7" viewBox="0 0 12 8"><path d="M1.5 1.5 6 6l4.5-4.5" fill="none" stroke="#2f3234" stroke-width="2"/></svg></div></div>
    <div class="select" style="left:110px;top:316px;width:85px;height:35px"><span>Min</span>
      <div class="chev" style="width:30px"><svg width="11" height="7" viewBox="0 0 12 8"><path d="M1.5 1.5 6 6l4.5-4.5" fill="none" stroke="#2f3234" stroke-width="2"/></svg></div></div>
    <div class="select" style="left:199px;top:316px;width:85px;height:35px"><span>Sec</span>
      <div class="chev" style="width:30px"><svg width="11" height="7" viewBox="0 0 12 8"><path d="M1.5 1.5 6 6l4.5-4.5" fill="none" stroke="#2f3234" stroke-width="2"/></svg></div></div>

    <div class="field-label" style="top:363px;left:21px">Set date and location :</div>
    <div class="select tiny" style="left:21px;top:397px;width:50px;height:35px"><span>DD</span>
      <div class="chev" style="width:19px"><svg width="8" height="6" viewBox="0 0 12 8"><path d="M1.5 1.5 6 6l4.5-4.5" fill="none" stroke="#2f3234" stroke-width="2.4"/></svg></div></div>
    <div class="select tiny" style="left:75px;top:397px;width:50px;height:35px"><span>MM</span>
      <div class="chev" style="width:19px"><svg width="8" height="6" viewBox="0 0 12 8"><path d="M1.5 1.5 6 6l4.5-4.5" fill="none" stroke="#2f3234" stroke-width="2.4"/></svg></div></div>
    <div class="select tiny" style="left:129px;top:397px;width:50px;height:35px"><span>YYYY</span>
      <div class="chev" style="width:19px"><svg width="8" height="6" viewBox="0 0 12 8"><path d="M1.5 1.5 6 6l4.5-4.5" fill="none" stroke="#2f3234" stroke-width="2.4"/></svg></div></div>
    <div class="select" style="left:188px;top:397px;width:96px;height:35px;font-size:10px"><span style="padding-left:7px">Your location</span>
      <div class="chev" style="width:19px"><svg width="8" height="6" viewBox="0 0 12 8"><path d="M1.5 1.5 6 6l4.5-4.5" fill="none" stroke="#2f3234" stroke-width="2.4"/></svg></div></div>

    <div class="field-label" style="top:445px">We will come to you :</div>
    <div class="note"></div>
    <div class="submit">SUBMIT</div>
  </form>

  <section class="about">
    <div class="about-kicker">ABOUT</div>
    <h2 class="about-title"><b>GADGET</b> <em>HAVEN</em></h2>
    <div class="about-device" role="img" aria-label="Silver smartphone with a blue home screen"></div>
    <div class="about-copy">
      <p><strong>Lorem ipsum dolor sit amet, consectetur adipiscing elit.</strong> Mauris non varius urna, sit amet tincidunt risus. Mauris vulputate aliquet rhoncus. Pellentesque semper massa ut enim interdum, fringilla sceler­isque tellus semper. Praesent in purus bibendum, efficitur nulla a, sagittis turpis. Sed et mi eget est varius feugiat rhoncus interdum justo. Mauris scelerisque ex eu vulputate gravida. Fusce luctus con­vallis scelerisque. Donec quis enim dolor. Proin sit amet augue neque.</p>
      <p>Suspendisse id tincidunt ligula. <strong>Phasellus imperdiet, nulla sed auctor tincidunt,</strong> mauris nisl ultrices turpis, quis lacinia tortor nulla bibendum sem. Phasellus vehicula, ante in feugiat sollicitudin, tortor magna rutrum dui, eu placerat orci dolor commodo nunc. Morbi ut risus nec est commodo sodales. Aenean blandit, lacus in gravida accumsan, lectus libero pretium velit, et pulvinar metus diam id nisi. Sed at bibendum ipsum, non vehicula libero. Nunc a accumsan mi.</p>
      <p>Morbi in iaculis sapien, ut auctor diam. Proin vitae mauris vitae orci consequat volutpat et vitae diam. Nullam porta justo a odio maximus dictum. Suspendisse bibendum aliquet rhoncus.</p>
    </div>
    <div class="read-more">READ MORE</div>
  </section>

</div>
</body>
</html>
```